Kettle Ledger Business Card design

We need a stand out business card design for Accounting practice based in Australia specialising in pubs, clubs and hotels. We help venues maximise margins, create time and manage cashflow. One club we have been working with for the last 6 months has increased revenue by 3% and margin by 5% in this time frame. We have a back office outsourced system that costs less than having a full time employee and also allows the venues the added benefit of:<br/>-using the office space to become a revenue generating opportunity. <br/>-a complete system to enhance governance, accountability and efficiency within their operation<br/>-52 weeks cover so no hassle to cover annual/sick .. leave<br/><br/>We would like to see designs that use the colours of our logo (green & blue).
Target Market(s)
Australian Pubs, Clubs & Hotels abookkeeping, accounting and tax services
Industry/Entity Type
Accountant
Contact Information for Business Card
Miriam Oakley CPA
Principal
Accountant Tax Agent
Miriam@KettleLedger-example.com.au
0418693142
www.kettleledger-example.com.au
Accounting / Payroll / Tax / SMSF / Technology
Colors
Designer to choose colors to be used in the design.
Look and feel
Each slider illustrates characteristics of the customer's brand and the style your logo design should communicate.

```html
<!DOCTYPE html>
<html lang="en">
<head>
<meta charset="utf-8">
<title>Kettle Ledger Business Card</title>
<link href="https://fonts.googleapis.com/css2?family=Poppins:wght@400;500;600;700&display=swap" rel="stylesheet">
<style>
  :root {
    --brand-blue: #253f94;
    --brand-green: #1a7a3c;
    --card-white: #ffffff;
    --backdrop: #e6e7ea;
    --text-light: #ffffff;
  }
  * { box-sizing: border-box; margin: 0; padding: 0; }
  html, body {
    width: 1200px; height: 880px; overflow: hidden;
    background: var(--backdrop);
    font-family: "Poppins", sans-serif;
  }
  .canvas {
    width: 1200px; height: 880px;
    display: flex; flex-direction: column; align-items: center; justify-content: center;
    gap: 48px;
  }
  .card {
    width: 630px; height: 360px;
    background: var(--card-white);
    border-radius: 18px;
    position: relative; overflow: hidden;
    box-shadow: 0 6px 20px rgba(0,0,0,0.12);
  }
  .brand-lockup { display: flex; align-items: center; gap: 14px; }
  .brand-mark {
    width: 54px; height: 54px; border-radius: 50%;
    background: var(--brand-green);
  }
  .brand-name {
    font-weight: 700; color: var(--brand-blue);
    font-size: 46px; letter-spacing: -0.5px; line-height: 1;
  }
  .card-front { display: flex; align-items: center; justify-content: center; }

  .card-back .logo-area {
    height: 160px; display: flex; align-items: center; justify-content: center;
  }
  .card-back .brand-mark { width: 46px; height: 46px; }
  .card-back .brand-name { font-size: 40px; }
  .info-band {
    position: absolute; left: 0; right: 0; top: 160px; height: 150px;
    background: var(--brand-blue); color: var(--text-light);
    display: flex; align-items: center; justify-content: center; gap: 22px;
  }
  .person { text-align: right; }
  .person-name { font-weight: 600; font-size: 20px; }
  .person-role { font-size: 13px; line-height: 1.35; }
  .divider { width: 2px; height: 74px; background: var(--text-light); }
  .contacts { list-style: none; font-size: 13px; line-height: 1.75; }
  .contacts li { display: flex; align-items: center; gap: 8px; }
  .contacts svg { width: 13px; height: 13px; flex: none; }
  .services {
    position: absolute; left: 0; right: 0; top: 310px; height: 50px;
    display: flex; align-items: center; justify-content: center;
    color: var(--brand-green); font-size: 14px; letter-spacing: 1px;
  }
</style>
</head>
<body>
<main class="canvas">
  <section class="card card-front">
    <div class="brand-lockup">
      <span class="brand-mark"></span>
      <span class="brand-name">Kettle Ledger</span>
    </div>
  </section>

  <section class="card card-back">
    <div class="logo-area">
      <div class="brand-lockup">
        <span class="brand-mark"></span>
        <span class="brand-name">Kettle Ledger</span>
      </div>
    </div>
    <div class="info-band">
      <div class="person">
        <p class="person-name">Miriam Oakley CPA</p>
        <p class="person-role">Principal</p>
        <p class="person-role">Accountant Tax Agent</p>
      </div>
      <span class="divider"></span>
      <ul class="contacts">
        <li>
          <svg viewBox="0 0 16 16"><rect x="1" y="3" width="14" height="10" fill="#fff"/><path d="M1 3l7 6 7-6" fill="none" stroke="#253f94" stroke-width="1.5"/></svg>
          Miriam@KettleLedger-example.com.au
        </li>
        <li>
          <svg viewBox="0 0 16 16"><rect x="4" y="1" width="8" height="14" rx="1.5" fill="none" stroke="#fff" stroke-width="1.5"/></svg>
          0418693142
        </li>
        <li>
          <svg viewBox="0 0 16 16"><circle cx="8" cy="8" r="6.5" fill="none" stroke="#fff" stroke-width="1.3"/><ellipse cx="8" cy="8" rx="3" ry="6.5" fill="none" stroke="#fff" stroke-width="1"/><path d="M1.5 8h13" stroke="#fff" stroke-width="1"/></svg>
          www.kettleledger-example.com.au
        </li>
      </ul>
    </div>
    <p class="services">Accounting / Payroll / Tax / SMSF / Technology</p>
  </section>
</main>
</body>
</html>
```